WEB PAGES DESIGN

We need a web design for a new company called "NUBRA42". Our major business is that provide Internet Data Center solution, such as: rack/colocation, bandwidth, dedicated server, cloud server, CDN, and so on.
Requirements of Design:
1. Home page layout can refer to index-content.jpg in the attachments, but not limited.
2. According to match logo colors to design colors of web pages, Logo in the attachments.
3. The web contents of home page in image of the index-content.jpg.
4. The successful bidder will need to design three banner.
Industry/Entity Type
Business

```html
<!DOCTYPE html>
<html lang="en">
<head>
<meta charset="utf-8">
<title>NUBRA42 – IDC Solutions</title>
<link href="https://fonts.googleapis.com/css2?family=Arvo:wght@700&family=Questrial&display=swap" rel="stylesheet">
<style>
:root{
  --green:#8cc63f;
  --green-dark:#4f7a1e;
  --green-pale:#d9f5ae;
  --charcoal:#444444;
  --ink:#333333;
  --text:#4a4a4a;
  --page:#f5f8fa;
  --card:#eef1f3;
  --white:#ffffff;
  --backdrop-1:#2f6a2c;
  --backdrop-2:#12361a;
}
*{margin:0;padding:0;box-sizing:border-box}
html,body{width:737px;height:1200px;overflow:hidden}
body{
  position:relative;
  font-family:"Questrial",Arial,sans-serif;
  background:radial-gradient(ellipse at center,var(--backdrop-1) 0%,var(--backdrop-2) 100%);
  color:var(--text);
}
h1,h2,h3,h4{font-weight:400}
.abs{position:absolute}
.page{position:absolute;left:86px;top:0;width:561px;height:1200px;background:var(--page)}
.top-band{left:0;top:0;width:561px;height:16px;background:var(--green)}
.header-rule{left:0;top:80px;width:561px;height:2px;background:#3a3a3a}

.brand{display:flex;align-items:center;gap:5px}
.brand-mark{width:12px;height:12px;background:var(--green)}
.brand-name{font-size:13px;color:var(--ink);letter-spacing:.5px}
.brand.stacked{flex-direction:column;gap:6px;width:80px}
.brand.stacked .brand-name{font-size:12px}

.nav{left:170px;top:64px;display:flex;font-size:9px;color:var(--ink)}
.nav a{color:inherit;text-decoration:none;height:16px;line-height:16px;padding:0 9px;margin-right:4px}
.nav a.active{background:var(--charcoal);color:var(--white);border-radius:2px 2px 0 0;padding:0 13px;margin-right:6px}

.hero{left:0;top:82px;width:561px;height:278px;background:var(--green)}
.hero-photo{left:0;top:0;width:210px;height:278px;
  background:linear-gradient(90deg,#3b5a30 0%,#6f9a55 55%,rgba(140,198,63,0) 100%)}
.hero-title{left:209px;top:84px;width:233px;height:50px;background:var(--green-pale);
  font-family:"Arvo",Georgia,serif;font-weight:700;font-size:25px;color:#2e2e2e;line-height:50px;padding-left:10px;letter-spacing:.5px}
.hero-copy{left:209px;top:140px;width:310px;font-size:14.5px;line-height:16.5px;color:var(--white)}
.btn-light{left:210px;top:200px;width:89px;height:22px;background:linear-gradient(#fafafa,#d4d4d4);
  font-size:9.5px;color:var(--ink);text-align:center;line-height:22px;border-radius:2px}
.slide-arrow{width:18px;height:18px;background:var(--green-dark);border-radius:2px}
.dots{left:277px;top:258px;display:flex;gap:4px}
.dots span{width:5px;height:5px;border-radius:50%;background:#3c4a30}
.hero-shadow{left:10px;top:360px;width:540px;height:14px;
  background:radial-gradient(ellipse at top,rgba(0,0,0,.22),rgba(0,0,0,0) 70%)}

.section-title{left:63px;top:367px;font-size:18px;color:var(--ink)}

.card{width:212px;height:209px;background:var(--card);border:1px solid #cfd4d7;box-shadow:0 1px 2px rgba(0,0,0,.1)}
.card-photo{left:0;top:0;width:210px;height:111px;background:linear-gradient(120deg,#2b2b2b 0%,#6a6e73 45%,#9aa3ab 70%,#1c1c1c 100%)}
.card-tab{left:0;top:0;height:38px;padding:0 14px;line-height:36px;font-size:14px;color:var(--white);background:var(--green);min-width:152px}
.card-tab.dark{background:#3d3d3d}
.card-copy{left:15px;top:120px;width:185px;font-size:8.2px;line-height:12px;color:var(--text)}
.btn-more{left:15px;top:176px;width:67px;height:22px;border-radius:3px;background:var(--green);
  color:var(--white);font-size:8px;line-height:22px;text-align:center}
.btn-more.dark{background:#3d3d3d}

.partner-band{left:0;top:856px;width:561px;height:109px;background:var(--charcoal)}
.partner-photo{left:69px;top:845px;width:190px;height:127px;border:4px solid var(--green);
  background:linear-gradient(135deg,#dfe6ea,#9fb0bb 60%,#c9d4da)}
.partner-title{left:270px;top:867px;font-size:13px;color:var(--green)}
.partner-rule{left:270px;top:888px;width:218px;height:1px;background:#6a6a6a}
.partner-copy{left:271px;top:893px;width:210px;font-size:8.5px;line-height:13px;color:var(--white)}

.help-bar{left:59px;top:983px;width:437px;height:42px;background:#f0f2f3;border:1px solid #c9cdd0}
.help-text{left:34px;top:0;line-height:40px;font-size:10px;color:var(--ink);letter-spacing:.2px}

.foot-box{background:var(--white)}
.foot-title{font-size:11px;color:var(--ink)}
.news-list{list-style:none;font-size:6.8px;color:var(--text)}
.news-list li{position:relative;padding-left:14px;height:14px}
.news-list li::before{content:"";position:absolute;left:2px;top:1px;border-left:4px solid var(--green);border-top:3px solid transparent;border-bottom:3px solid transparent}
.contact{font-size:7.5px;color:var(--ink);line-height:12px}
.social{display:flex;gap:12px}
.social span{width:26px;height:26px;border-radius:50%;background:var(--ink)}
.copy-bar{left:0;top:1175px;width:561px;height:25px;font-size:6px;color:var(--ink)}
</style>
</head>
<body>
<div class="page">
  <div class="abs top-band"></div>

  <div class="abs brand" style="left:67px;top:40px">
    <span class="brand-mark"></span><span class="brand-name">NUBRA42</span>
  </div>

  <nav class="abs nav">
    <a class="active">Home</a><a>Dedicated server</a><a>Hosting</a><a>Data Center</a><a>About Us</a>
  </nav>
  <div class="abs header-rule"></div>

  <section class="abs hero">
    <div class="abs hero-photo" role="img" aria-label="Smiling businessman with folded arms in front of data center server racks"></div>
    <h1 class="abs hero-title">IDC SOLUTIONS</h1>
    <p class="abs hero-copy">NUBRA42 provides a wide range of highly specialized solutions that utilizes technology to transform your organization</p>
    <div class="abs btn-light">Read more</div>
    <svg class="abs slide-arrow" style="left:15px;top:119px" viewBox="0 0 18 18"><path d="M11 5 L7 9 L11 13" stroke="#fff" stroke-width="2" fill="none"/></svg>
    <svg class="abs slide-arrow" style="left:523px;top:119px" viewBox="0 0 18 18"><path d="M7 5 L11 9 L7 13" stroke="#fff" stroke-width="2" fill="none"/></svg>
    <div class="abs dots"><span></span><span></span><span></span></div>
  </section>
  <div class="abs hero-shadow"></div>

  <h2 class="abs section-title">Our Products</h2>

  <article class="abs card" style="left:58px;top:397px">
    <div class="abs card-photo" role="img" aria-label="Business handshake in front of office windows"></div>
    <h3 class="abs card-tab dark">Dedicated Servers</h3>
    <p class="abs card-copy">Lorem gubergren amet at consetetur ut illum ea dignissim dolores. Sed at commodo vero in dolore dolor kasd gubergren. Diam labore molestie sadipscing labore ipsum dolores.</p>
    <div class="abs btn-more dark">read more »</div>
  </article>

  <article class="abs card" style="left:282px;top:397px">
    <div class="abs card-photo" role="img" aria-label="Business handshake in front of office windows"></div>
    <h3 class="abs card-tab">Servers Hosting</h3>
    <p class="abs card-copy">Lorem gubergren amet at consetetur ut illum ea dignissim dolores. Sed at commodo vero in dolore dolor kasd gubergren. Diam labore molestie sadipscing labore ipsum dolores.</p>
    <div class="abs btn-more">read more »</div>
  </article>

  <article class="abs card" style="left:58px;top:616px">
    <div class="abs card-photo" role="img" aria-label="Business handshake in front of office windows"></div>
    <h3 class="abs card-tab">Rack &amp;Bandwidth</h3>
    <p class="abs card-copy">Lorem gubergren amet at consetetur ut illum ea dignissim dolores. Sed at commodo vero in dolore dolor kasd gubergren. Diam labore molestie sadipscing labore ipsum dolores.</p>
    <div class="abs btn-more">read more »</div>
  </article>

  <article class="abs card" style="left:282px;top:616px">
    <div class="abs card-photo" role="img" aria-label="Business handshake in front of office windows"></div>
    <h3 class="abs card-tab">Reseller &amp; Referral</h3>
    <p class="abs card-copy">Lorem gubergren amet at consetetur ut illum ea dignissim dolores. Sed at commodo vero in dolore dolor kasd gubergren. Diam labore molestie sadipscing labore ipsum dolores.</p>
    <div class="abs btn-more">read more »</div>
  </article>

  <section>
    <div class="abs partner-band"></div>
    <div class="abs partner-photo" role="img" aria-label="Smiling businessman giving thumbs up with colleagues in an office"></div>
    <h3 class="abs partner-title">Our New Partner</h3>
    <div class="abs partner-rule"></div>
    <p class="abs partner-copy">Lorem gubergren amet at consetetur ut illum ea dignissim dolores. Sed at commodo vero in dolore dolor kasd gubergren. Diam labore molestie sadipscing labore ipsum dolores.</p>
    <svg class="abs" style="left:463px;top:947px" width="22" height="12" viewBox="0 0 22 12"><path d="M6 1 L1 6 L6 11Z M16 1 L21 6 L16 11Z" fill="#fff"/></svg>
  </section>

  <div class="abs help-bar">
    <svg class="abs" style="left:-1px;top:-1px" width="32" height="42" viewBox="0 0 32 42"><path d="M0 0 H14 L31 21 L14 42 H0Z" fill="var(--green)"/></svg>
    <p class="abs help-text">NEED HELP? CALL OUR AWARD-WINNING SUPPORT TEAM 24/7 AT 555-014-2290</p>
  </div>

  <section class="abs foot-box" style="left:0;top:1040px;width:241px;height:135px">
    <h4 class="abs foot-title" style="left:61px;top:13px">Latest New</h4>
    <ul class="abs news-list" style="left:61px;top:36px">
      <li>Lorem gubergren amet at consetetur ut illum</li>
      <li>ea dignissim dolores. Sed at commodo vero</li>
      <li>in dolore dolor kasd gubergren. Diam labore</li>
      <li>molestie sadipscing labore ipsum dolores.</li>
      <li>Takimata ea consectetuer magna.</li>
    </ul>
  </section>

  <div class="abs brand stacked" style="left:241px;top:1088px">
    <span class="brand-mark"></span><span class="brand-name">NUBRA42</span>
  </div>

  <section class="abs foot-box" style="left:321px;top:1040px;width:240px;height:135px">
    <h4 class="abs foot-title" style="left:13px;top:10px">Contact Us</h4>
    <div class="abs contact" style="left:15px;top:32px">
      <div style="font-size:10px">NUBRA42</div>
      <div>4410 Orchard Lane</div>
      <div>Millbrook, TX 70412</div>
      <div style="font-size:10px">Phone: 555-014-2290</div>
    </div>
    <span class="abs" style="left:133px;top:37px;width:26px;height:26px;border-radius:50%;background:var(--green)"></span>
    <div class="abs social" style="left:13px;top:97px"><span></span><span></span><span></span><span></span></div>
  </section>

  <footer class="abs copy-bar">
    <span class="abs" style="left:60px;top:8px">Copyright © 1999 - 2015 NUBRA42 . All Rights Reserved.</span>
    <span class="abs" style="left:336px;top:8px">Terms of Service | Privacy Policy | Contact Us</span>
  </footer>
</div>
</body>
</html>
```